Luxury Skincare Product Box Packaging Design

Vorabelle is a range of skincare products that help protect, nourish, and strengthen even the most sensitive skin, ensuring it is healthy, glowing, calm, and soft. Skincare practices support skin to enhance its appearance and relieve skin conditions. Your skin reflects your health. It is your body canvas and is an asset. The products contain naturally derived ingredients, aromatherapy oils, sustainable and ethical ingredients, organic ingredients where possible, natural preservatives and Australian oils, fruits, and extracts.

Vorabelle
Tagline is "Where Calm Finds Bloom"

Our products do not contain sulphates, parabens, phthalates, petrochemicals, synthetic colours, nor synthetic fragrances.

Everything about the Vorabelle Skincare name is creative and communicates luxury. Vorabelle from your first glance of the name, you will know that this is a company with excellent products.

By keeping it simple, unique, and elegant is often associated with high quality and is a way to establish trust. Vorabelle is a product that is “pure” and natural, so Vorabelle packaging would look simple, elegant, and clean.

I have uploaded the actual logo design and individual labels for the current skincare range I currently with the ingredients included so you can get an understanding of what I like. I have also added samples of package designs I quite like to assist with your designs.

Each Product box packaging sizes are as follows:

Product One - Exfoliating Herbs: 110mm (H) x 33mm Diameter
Product Two - Probiotic Lotion: 138mm (H) x 33mm Diameter
Product Three - Vitamin A Serum: 120mm (H) x 30mm Diameter
Updates

The Measurements are as follows: Product One: 110mm (H) x 33mm Diameter Product Two: 138mm (H) x 33mm Diameter Product Three: 120mm (H) x 30mm Diameter

Target Market(s)

Women

Requirements
Must have
• Logo, Product Name and ingredients and if you can barcode on the packaging that is the box design I am after
Nice to have
• samples of designs I like but open to suggestions

```html
<!DOCTYPE html>
<html lang="en">
<head>
<meta charset="utf-8">
<title>Vorabelle Skincare – Box Dielines</title>
<link href="https://fonts.googleapis.com/css2?family=Montserrat:wght@300;400;600;700&family=Roboto+Condensed:wght@400;700&display=swap" rel="stylesheet">
<style>
  :root{
    --backdrop:#e5d5c3;
    --card:#ffffff;
    --cut:#4a4a4a;
    --ink:#1e1e1e;
    --rose:#c08a72;
    --petal:#ececec;
    --petal-edge:#f7f7f7;
  }
  *{margin:0;padding:0;box-sizing:border-box}
  html,body{width:960px;height:1200px;overflow:hidden;background:var(--backdrop)}
  .canvas{position:relative;width:960px;height:1200px;font-family:"Montserrat",sans-serif;color:var(--ink)}
  .dieline{position:absolute;left:0;top:0}
  .dieline polygon,.dieline rect,.dieline path{fill:var(--card);stroke:var(--cut);stroke-width:.6}
  .dieline line{stroke:var(--cut);stroke-width:.6}
  .block{position:absolute}
  .ingredients{font-size:5.6px;line-height:9.7px;text-transform:uppercase;letter-spacing:-.05px}
  .ingredients b{font-weight:700;font-size:6.4px}
  .ingredients .organic{font-weight:700;display:block;padding-left:2px}
  .ingredients.bold-set{font-family:"Roboto Condensed",sans-serif;font-size:8.9px;line-height:9.7px;letter-spacing:0}
  .ingredients.bold-set b{font-size:8.9px}
  .caution{border:.7px solid var(--ink);border-radius:4px;font-size:4.5px;line-height:6.3px;padding:3px 3px}
  .skin-note{font-size:8.6px;line-height:8.5px}
  .directions{font-size:8.4px;line-height:11.7px}
  .directions h3{display:inline;font-size:10.2px;font-weight:600}
  .product-name{text-align:center;font-weight:300;font-size:10.4px;line-height:13.5px}
  .skin-type{text-align:center;font-weight:300;font-size:6px}
  .volume{text-align:center;font-weight:300;font-size:7.4px}
  .url{text-align:center;font-size:5.6px}
  .wordmark{color:var(--rose);font-weight:300;letter-spacing:1.2px;white-space:nowrap;text-align:center}
  .wordmark.vertical{transform:rotate(-72deg);transform-origin:center}
  .floral{position:absolute;border-radius:45%;background:radial-gradient(circle at 50% 50%,var(--petal-edge) 0%,var(--petal) 60%,rgba(236,236,236,0) 100%)}
  .icons{position:absolute;display:flex;justify-content:space-between}
  .icon{width:16px;text-align:center;font-size:2.6px;line-height:3px}
  .icon svg{display:block;margin:0 auto 1px;width:10px;height:10px}
  .icon svg *{fill:none;stroke:var(--ink);stroke-width:1}
</style>
</head>
<body>
<div class="canvas">

<svg class="dieline" width="960" height="1200" viewBox="0 0 960 1200">
  <!-- Vitamin A Serum box -->
  <polygon points="64,122 32,141 32,463 64,487"/>
  <polygon points="64,122 75,111 75,55 152,55 152,120 155,122"/>
  <path d="M155,122 V14 Q155,10 159,10 H243 Q247,10 247,14 V122 Z"/>
  <line x1="155" y1="31" x2="247" y2="31"/>
  <polygon points="247,122 249,120 249,55 327,55 327,111 338,122"/>
  <rect x="64" y="122" width="91" height="365"/>
  <rect x="155" y="122" width="92" height="365"/>
  <rect x="247" y="122" width="91" height="365"/>
  <rect x="338" y="122" width="91" height="365"/>
  <polygon points="64,487 75,498 75,555 152,555 152,489 155,487"/>
  <polygon points="247,487 249,489 249,555 327,555 327,498 338,487"/>
  <path d="M338,487 V595 Q338,599 342,599 H425 Q429,599 429,595 V487 Z"/>
  <line x1="338" y1="579" x2="429" y2="579"/>

  <!-- Probiotic Lotion box -->
  <polygon points="540,175 511,189 511,579 540,595"/>
  <polygon points="540,175 552,164 552,100 637,100 637,173 641,175"/>
  <path d="M641,175 V62 Q641,58 645,58 H737 Q741,58 741,62 V175 Z"/>
  <line x1="641" y1="74" x2="741" y2="74"/>
  <polygon points="741,175 744,173 744,100 829,100 829,164 841,175"/>
  <rect x="540" y="175" width="101" height="420"/>
  <rect x="641" y="175" width="100" height="420"/>
  <rect x="741" y="175" width="100" height="420"/>
  <rect x="841" y="175" width="101" height="420"/>
  <polygon points="540,595 552,606 552,669 637,669 637,597 641,595"/>
  <polygon points="741,595 744,597 744,669 829,669 829,606 841,595"/>
  <path d="M841,595 V708 Q841,712 845,712 H938 Q942,712 942,708 V595 Z"/>
  <line x1="841" y1="695" x2="942" y2="695"/>

  <!-- Exfoliating Herbs box -->
  <polygon points="259,727 233,735 233,1055 259,1062"/>
  <polygon points="259,727 271,716 271,652 356,652 356,725 360,727"/>
  <path d="M360,727 V614 Q360,610 364,610 H456 Q460,610 460,614 V727 Z"/>
  <line x1="360" y1="627" x2="460" y2="627"/>
  <polygon points="460,727 464,725 464,652 549,652 549,716 561,727"/>
  <rect x="259" y="727" width="101" height="335"/>
  <rect x="360" y="727" width="100" height="335"/>
  <rect x="460" y="727" width="101" height="335"/>
  <rect x="561" y="727" width="100" height="335"/>
  <polygon points="259,1062 271,1073 271,1137 356,1137 356,1064 360,1062"/>
  <polygon points="460,1062 464,1064 464,1137 549,1137 549,1073 561,1062"/>
  <path d="M561,1062 V1175 Q561,1179 565,1179 H657 Q661,1179 661,1175 V1062 Z"/>
  <line x1="561" y1="1162" x2="661" y2="1162"/>
</svg>

<!-- ===== Vitamin A Serum ===== -->
<div class="block ingredients" style="left:70px;top:191px;width:84px">
  <b>Ingredients: :</b><br>
  Simmondsia chinensis (jojoba) seed oil*, persea gratissima (avocado) oil, rosa eglanteria (rosehip) oil*, olea europaea (olive) fruit oil*, hippophae rhamnoides (seabuckthorn berry) kernal extract*, tocopherol (vitamin E), retinyl palmitate (vitamin A), glycine soja oilboswellia carterii oil (frankincense), pelargonium roseum leaf oil, (rose geranium), cananga odorata flower oil (ylang ylang), rosmarinus officianlis leaf extract
  <span class="organic">*Organic ingredients</span>
</div>
<div class="block caution" style="left:66px;top:423px;width:87px;height:37px">Store in a cool dry place Caution For external use only. Avoid contact with eyes. If irritation occurs, discontinue use.</div>

<div class="floral" role="img" aria-label="Faint line drawing of wild rose blossoms" style="left:160px;top:200px;width:84px;height:180px"></div>
<div class="block wordmark vertical" style="left:140px;top:255px;width:120px;font-size:24px">Vorabelle</div>
<div class="block product-name" style="left:155px;top:407px;width:92px">Vitamin A<br>Serum</div>
<div class="block skin-type" style="left:155px;top:435px;width:92px">All Skin Types</div>
<div class="block volume" style="left:155px;top:465px;width:92px">30ml</div>

<div class="block skin-note" style="left:254px;top:188px;width:84px">All Skin Types -<br>Particularly<br>beneficial for dry,<br>Mature skins</div>
<div class="block directions" style="left:254px;top:242px;width:84px"><h3>Directions:</h3><br>Directions: Massage a small amount into your face at night, avoiding eye area. Follow with your favourite moisturiser. Please note: Do not use on pregnant or breast-feeding women.</div>

<div class="icons" style="left:250px;top:405px;width:84px">
  <div class="icon"><svg viewBox="0 0 10 10"><circle cx="5" cy="5.5" r="3.6"/></svg>Australian Made</div>
  <div class="icon"><svg viewBox="0 0 10 10"><path d="M5 8.5 L1.5 5 A2 2 0 0 1 5 2.5 A2 2 0 0 1 8.5 5 Z"/></svg>100% Vegan</div>
  <div class="icon"><svg viewBox="0 0 10 10"><rect x="2" y="2" width="6" height="6" rx="3"/></svg>Cruelty Free</div>
  <div class="icon"><svg viewBox="0 0 10 10"><polygon points="5,1.5 8.8,8 1.2,8"/></svg>Please Recycle</div>
  <div class="icon"><svg viewBox="0 0 10 10"><rect x="2" y="3" width="6" height="5.5"/><line x1="1.5" y1="3" x2="8.5" y2="1.5"/></svg>6 months once open</div>
</div>
<div class="block url" style="left:247px;top:450px;width:91px">www.vorabelle.com</div>

<div class="floral" role="img" aria-label="Faint outline of a wild rose" style="left:343px;top:204px;width:82px;height:76px"></div>
<div class="block wordmark" style="left:338px;top:311px;width:91px;font-size:12px">Vorabelle</div>
<div class="floral" role="img" aria-label="Faint outline of a wild rose" style="left:343px;top:350px;width:82px;height:80px"></div>

<!-- ===== Probiotic Lotion ===== -->
<div class="block ingredients" style="left:545px;top:258px;width:94px">
  <b>Ingredients:</b> Aloe barbadensis (aloe vera) leaf juice, rosa eglanteria (rosehip) oil*, coco-glucoside, agave americana leaf extract, lactobacillus bulgaricus ferment filtrate, eucalyptus globulus (tasmanian blue gum extract) stearic acid (vegetable derived), glyceryl stearate (vegetable derived), glycerin*, cucumis sativus (cucumber) seed oil, salix alba (white willow bark), xanthus gum, cetearyl alcohol (coconut derived), terimінalia origanum vulgare oil, thymus vulgaris extract, olea europeia leaf extract, rosmarinus officinalis leaf extract, lavandula angustifolia (lavender) flower extract, pelargonium graveolens (geranium) oil
  <span class="organic">*Organic ingredients</span>
</div>

<div class="floral" role="img" aria-label="Faint botanical drawing of leaves and berries" style="left:644px;top:236px;width:94px;height:150px"></div>
<div class="block wordmark vertical" style="left:630px;top:320px;width:122px;font-size:25px">Vorabelle</div>

<div class="block skin-note" style="left:750px;top:262px;width:90px">All Skin Types -<br>Innovative<br>moisturising lotion<br>soothes and settles<br>problematic and<br>blemish prone<br>complexions.</div>
<div class="block directions" style="left:748px;top:344px;width:90px"><h3>Directions:</h3> Apply a small amount to your face morning and night after cleansing. Avoid eye area.</div>

<div class="icons" style="left:742px;top:524px;width:98px">
  <div class="icon"><svg viewBox="0 0 10 10"><circle cx="5" cy="5.5" r="3.6"/></svg>Australian Made</div>
  <div class="icon"><svg viewBox="0 0 10 10"><path d="M5 8.5 L1.5 5 A2 2 0 0 1 5 2.5 A2 2 0 0 1 8.5 5 Z"/></svg>100% Vegan</div>
  <div class="icon"><svg viewBox="0 0 10 10"><rect x="2" y="2" width="6" height="6" rx="3"/></svg>Cruelty Free</div>
  <div class="icon"><svg viewBox="0 0 10 10"><polygon points="5,1.5 8.8,8 1.2,8"/></svg>Please Recycle</div>
  <div class="icon"><svg viewBox="0 0 10 10"><rect x="2" y="3" width="6" height="5.5"/><line x1="1.5" y1="3" x2="8.5" y2="1.5"/></svg>6 months once open</div>
</div>

<div class="block wordmark" style="left:841px;top:374px;width:101px;font-size:14px">Vorabelle</div>
<div class="floral" role="img" aria-label="Faint botanical drawing of leaves and berries" style="left:846px;top:408px;width:92px;height:130px"></div>

<!-- ===== Gentle Exfoliating Herbs ===== -->
<div class="block ingredients bold-set" style="left:263px;top:794px;width:96px">
  <b>Ingredients:</b> Oryza sativa (rice) powder*, rosa gallica (rose petals)*, jasminum officinale (jasmine) flower, matricaria recutita (chamomile flowers)*, camellia sinensis leaf (green tea), luffa cylindrica fruit powder, calendula officinalis (marigold flowers) <span class="organic">*Organic ingredients</span>
</div>
<div class="block caution" style="left:266px;top:977px;width:88px;height:39px">Store in a cool dry place Caution For external use only. Avoid contact with eyes. If irritation occurs, discontinue use.</div>

<div class="floral" role="img" aria-label="Soft grey drawing of a rose in bloom" style="left:365px;top:786px;width:90px;height:172px"></div>
<div class="block wordmark vertical" style="left:350px;top:855px;width:122px;font-size:25px">Vorabelle</div>
<div class="block product-name" style="left:360px;top:980px;width:100px">Gentle<br>Exfoliating Herbs</div>
<div class="block skin-type" style="left:360px;top:1009px;width:100px">All Skin Types</div>
<div class="block volume" style="left:360px;top:1030px;width:100px">40ml</div>

<div class="block skin-note" style="left:464px;top:797px;width:96px">All Skin Types -<br>Particularly beneficial<br>for Sensitive, stressed<br>and delicate skins</div>
<div class="block directions" style="left:466px;top:867px;width:94px"><h3>Directions:</h3> Mix a small amount with your favourite cleanser. Massage into your face for approxi-mately one minute before removing with water or a face cloth. Use twice weekly.</div>

<div class="icons" style="left:461px;top:994px;width:98px">
  <div class="icon"><svg viewBox="0 0 10 10"><circle cx="5" cy="5.5" r="3.6"/></svg>Australian Made</div>
  <div class="icon"><svg viewBox="0 0 10 10"><path d="M5 8.5 L1.5 5 A2 2 0 0 1 5 2.5 A2 2 0 0 1 8.5 5 Z"/></svg>100% Vegan</div>
  <div class="icon"><svg viewBox="0 0 10 10"><rect x="2" y="2" width="6" height="6" rx="3"/></svg>Cruelty Free</div>
  <div class="icon"><svg viewBox="0 0 10 10"><polygon points="5,1.5 8.8,8 1.2,8"/></svg>Please Recycle</div>
  <div class="icon"><svg viewBox="0 0 10 10"><rect x="2" y="3" width="6" height="5.5"/><line x1="1.5" y1="3" x2="8.5" y2="1.5"/></svg>6 months once open</div>
</div>
<div class="block url" style="left:460px;top:1026px;width:101px">www.vorabelle.com</div>

<div class="block wordmark" style="left:561px;top:872px;width:100px;font-size:14px">Vorabelle</div>
<div class="floral" role="img" aria-label="Soft grey drawing of a rose in bloom" style="left:568px;top:915px;width:88px;height:106px"></div>

</div>
</body>
</html>
```